Mortgage Broker Site

Need a custom design for a mortgage broker site - please refer to the attached Word .doc that gives more detail.

Number of Pages Required

5+ page

Colors

Designer to choose colors to be used in the design.

```html
<!DOCTYPE html>
<html lang="en">
<head>
<meta charset="utf-8">
<title>Harbora — Mortgage Rates</title>
<link href="https://fonts.googleapis.com/css2?family=Raleway:wght@400;500;600;700&family=Roboto:wght@400;500;700&display=swap" rel="stylesheet">
<style>
:root{
  --white:#ffffff;
  --ink:#222222;
  --muted:#444444;
  --crimson:#9b1127;
  --sky:#aad3ed;
  --navy:#2d5a7b;
  --steel:#2f5f84;
  --violet:#8a58b5;
  --azure:#3498db;
  --divider:rgba(255,255,255,.3);
}
*{margin:0;padding:0;box-sizing:border-box}
html,body{width:1200px;height:2460px;overflow:hidden}
body{font-family:"Raleway",sans-serif;color:var(--ink);background:var(--white)}
.page{position:relative;width:1200px;height:2460px;overflow:hidden}

/* hero */
.hero{position:absolute;left:0;top:0;width:1200px;height:607px;color:var(--white)}
.hero-photo{position:absolute;inset:0;background:
  linear-gradient(180deg,rgba(20,25,20,.55) 0%,rgba(20,25,20,.35) 55%,rgba(20,25,20,.45) 100%),
  linear-gradient(180deg,#5d6a58 0%,#6f5a38 40%,#7a6236 62%,#4d5e2c 80%,#3f5222 100%)}
.nav{position:absolute;left:0;top:0;width:1200px;height:80px}
.brand{position:absolute;left:93px;top:18px;font-size:30px;font-weight:600;color:var(--white)}
.nav-links{position:absolute;left:228px;top:31px;display:flex;gap:26px;font-size:11px}
.nav-right{position:absolute;right:96px;top:32px;display:flex;align-items:center;gap:28px;font-size:11px}
.btn-apply{background:var(--crimson);padding:9px 15px;margin-left:-16px}
.hero-title{position:absolute;left:0;top:184px;width:1200px;text-align:center;font-size:44px;font-weight:700}
.hero-lead{position:absolute;left:280px;top:258px;width:640px;text-align:center;font-size:17px;line-height:22px}
.hero-actions{position:absolute;left:423px;top:360px;display:flex;gap:10px}
.hero-btn{width:153px;height:40px;border:2px solid var(--white);display:flex;align-items:center;justify-content:center;font-family:"Roboto",sans-serif;font-size:14px;font-weight:500}
.hero-btn.primary{background:var(--crimson)}

/* tools */
.tools{position:absolute;left:0;top:607px;width:1200px;height:441px}
.section-title{position:absolute;left:0;top:60px;width:1200px;text-align:center;font-size:28px;font-weight:400}
.section-sub{position:absolute;left:0;top:96px;width:1200px;text-align:center;font-size:15px;color:var(--muted)}
.tool-card{position:absolute;top:172px;width:308px;height:197px;background:var(--white);box-shadow:0 2px 14px rgba(0,0,0,.12);text-align:center}
.tool-card svg{position:absolute;left:50%;top:30px;transform:translateX(-50%)}
.tool-name{position:absolute;left:0;top:85px;width:100%;font-family:"Roboto",sans-serif;font-size:15px}
.tool-text{position:absolute;left:28px;top:117px;width:252px;font-size:11px;line-height:16px;color:var(--ink)}

/* limits */
.limits{position:absolute;left:0;top:1048px;width:1200px;height:253px;background:var(--sky);text-align:center}
.limits h2{position:absolute;left:0;top:52px;width:1200px;font-size:26px;font-weight:700;color:var(--navy)}
.limits p{position:absolute;left:220px;top:97px;width:760px;font-size:12.5px;line-height:18px;color:var(--steel);letter-spacing:.3px}
.search{position:absolute;left:324px;top:152px;display:flex;gap:6px}
.search-field{width:344px;height:38px;background:var(--white);font-size:9px;color:#5a8fb8;text-align:left;padding:13px 12px;letter-spacing:.4px}
.search-btn{width:127px;height:38px;background:var(--steel);color:var(--white);font-family:"Roboto",sans-serif;font-weight:500;font-size:13px;display:flex;align-items:center;justify-content:center}

/* contact */
.contact{position:absolute;left:0;top:1301px;width:1200px;height:251px;background:var(--violet);text-align:center}
.contact h2{position:absolute;left:0;top:74px;width:1200px;color:var(--white);font-size:27px;font-weight:700}
.phone-pill{position:absolute;left:396px;top:122px;width:408px;height:76px;border-radius:38px;background:var(--white);display:flex;align-items:center;justify-content:center;gap:12px;color:var(--violet);font-family:"Roboto",sans-serif;font-weight:500;font-size:44px}

/* photo */
.house-photo{position:absolute;left:0;top:1552px;width:1200px;height:480px;background:linear-gradient(180deg,#b9d8f1 0%,#a4c6e2 25%,#8d8474 45%,#c7bea9 62%,#6b6a55 78%,#4d7a32 100%)}

/* footer */
.footer{position:absolute;left:0;top:2032px;width:1200px;height:428px;background:var(--azure);color:var(--white)}
.footer-col{position:absolute;top:64px}
.footer-col h3{font-family:"Roboto",sans-serif;font-size:13px;font-weight:500;margin-bottom:6px}
.footer-col li{list-style:none;font-family:"Roboto",sans-serif;font-size:12.5px;line-height:23px;display:flex;align-items:center;gap:5px}
.footer-divider{position:absolute;top:50px;width:1px;height:166px;background:var(--divider)}
.footer-rule{position:absolute;left:0;top:241px;width:1200px;height:1px;background:var(--divider)}
.legal{position:absolute;left:0;top:256px;width:1200px;text-align:center;font-family:"Roboto",sans-serif;font-size:10px;font-weight:500;line-height:15px}
.footer-brand{position:absolute;left:0;top:298px;width:1200px;text-align:center;font-size:30px;font-weight:600}
</style>
</head>
<body>
<div class="page">

  <header class="hero">
    <div class="hero-photo" role="img" aria-label="Photo of a two-storey yellow house with a lawn and trees, darkened"></div>
    <nav class="nav">
      <div class="brand">Harbora</div>
      <div class="nav-links"><span>Rates</span><span>Purchase</span><span>Refinance</span></div>
      <div class="nav-right"><span>Schedule a Call</span><span>Guides</span><span class="btn-apply">Apply Now</span></div>
    </nav>
    <h1 class="hero-title">Mortgage Rates are at all time lows!</h1>
    <p class="hero-lead">Unknown printer took a galley of type and scrambled it to make a type speci-men book. It has survived not only five centuries, but also the</p>
    <div class="hero-actions">
      <span class="hero-btn">Purchase Rates</span>
      <span class="hero-btn primary">Refinance Rates</span>
    </div>
  </header>

  <section class="tools">
    <h2 class="section-title">MORTGAGE TOOLS</h2>
    <p class="section-sub">when an unknown printer took a galley of type and scrambled it to make a type specimen</p>

    <div class="tool-card" style="left:260px">
      <svg width="46" height="40" viewBox="0 0 46 40" aria-hidden="true">
        <path d="M23 2 L44 20 H39 V38 H7 V20 H2 Z" fill="#111"/>
        <rect x="32" y="4" width="5" height="10" fill="#111"/>
        <circle cx="17" cy="22" r="3.2" fill="#fff"/><circle cx="29" cy="31" r="3.2" fill="#fff"/>
        <path d="M30 19 L16 34" stroke="#fff" stroke-width="3"/>
      </svg>
      <div class="tool-name">Mortgage Calculator</div>
      <p class="tool-text">when an unknown printer took a galley of type and scrambled it to make a type.</p>
    </div>

    <div class="tool-card" style="left:607px">
      <svg width="42" height="28" viewBox="0 0 42 28" aria-hidden="true">
        <rect x="1" y="2" width="40" height="24" fill="none" stroke="#111" stroke-width="2"/>
        <path d="M1 8 A6 6 0 0 0 7 2 M35 2 A6 6 0 0 0 41 8 M1 20 A6 6 0 0 1 7 26 M35 26 A6 6 0 0 1 41 20" fill="none" stroke="#111" stroke-width="1.5"/>
        <text x="21" y="20" text-anchor="middle" font-family="Roboto,sans-serif" font-size="15" font-weight="700" fill="#111">$</text>
      </svg>
      <div class="tool-name">Home Value Checker</div>
      <p class="tool-text">when an unknown printer took a galley of type and scrambled it to make a type.</p>
    </div>
  </section>

  <section class="limits">
    <h2>2019 Mortgage Loan Limits For Conventional,FHA,&amp;VA Loans</h2>
    <p>Mortgage loan limits for every U.S.County,as published by Keystone Mae &amp; Freddie Housing Administration(FHA),and the Department of Veterans (VA)</p>
    <div class="search">
      <div class="search-field">SEARCH ANYTHING</div>
      <div class="search-btn">SEARCH</div>
    </div>
  </section>

  <section class="contact">
    <h2>Connect with America’s Lending Experts Today!</h2>
    <div class="phone-pill">
      <svg width="42" height="42" viewBox="0 0 42 42" aria-hidden="true" fill="none" stroke="#8a58b5" stroke-width="2" stroke-linecap="round">
        <path d="M10 6 L15 12 L12 16 C14 22 19 27 25 29 L29 26 L35 31 L31 36 C18 35 7 24 5 11 Z"/>
        <path d="M24 12 A7 7 0 0 1 30 18 M25 6 A13 13 0 0 1 36 17"/>
      </svg>
      <span>(800)555-0142</span>
    </div>
  </section>

  <div class="house-photo" role="img" aria-label="Photo of a new stone-front house with a wide white porch, garage and lawn under a blue sky"></div>

  <footer class="footer">
    <div class="footer-col" style="left:181px">
      <h3>LINKS</h3>
      <ul>
        <li><svg width="12" height="12" viewBox="0 0 12 12"><circle cx="6" cy="6" r="6" fill="#fff"/><path d="M3 6.2 L5.2 8.2 L9 4" stroke="#3498db" stroke-width="1.6" fill="none"/></svg>Get a Mortgage Rate Now</li>
        <li><svg width="12" height="12" viewBox="0 0 12 12"><circle cx="6" cy="6" r="6" fill="#fff"/><path d="M3 6.2 L5.2 8.2 L9 4" stroke="#3498db" stroke-width="1.6" fill="none"/></svg>Loan Types</li>
        <li><svg width="12" height="12" viewBox="0 0 12 12"><circle cx="6" cy="6" r="6" fill="#fff"/><path d="M3 6.2 L5.2 8.2 L9 4" stroke="#3498db" stroke-width="1.6" fill="none"/></svg>Harbora Disclosures</li>
        <li><svg width="12" height="12" viewBox="0 0 12 12"><circle cx="6" cy="6" r="6" fill="#fff"/><path d="M3 6.2 L5.2 8.2 L9 4" stroke="#3498db" stroke-width="1.6" fill="none"/></svg>Conforming, VA &amp; FHA Loan Limits</li>
      </ul>
    </div>
    <div class="footer-divider" style="left:471px"></div>
    <div class="footer-col" style="left:549px">
      <h3>COMPANY</h3>
      <ul>
        <li><svg width="12" height="12" viewBox="0 0 12 12"><circle cx="6" cy="6" r="6" fill="#fff"/><path d="M3 6.2 L5.2 8.2 L9 4" stroke="#3498db" stroke-width="1.6" fill="none"/></svg>About Us</li>
        <li><svg width="12" height="12" viewBox="0 0 12 12"><circle cx="6" cy="6" r="6" fill="#fff"/><path d="M3 6.2 L5.2 8.2 L9 4" stroke="#3498db" stroke-width="1.6" fill="none"/></svg>Careers</li>
        <li><svg width="12" height="12" viewBox="0 0 12 12"><circle cx="6" cy="6" r="6" fill="#fff"/><path d="M3 6.2 L5.2 8.2 L9 4" stroke="#3498db" stroke-width="1.6" fill="none"/></svg>Harbora Resources</li>
        <li><svg width="12" height="12" viewBox="0 0 12 12"><circle cx="6" cy="6" r="6" fill="#fff"/><path d="M3 6.2 L5.2 8.2 L9 4" stroke="#3498db" stroke-width="1.6" fill="none"/></svg>Contact</li>
      </ul>
    </div>
    <div class="footer-divider" style="left:764px"></div>
    <div class="footer-col" style="left:874px">
      <h3>POLICIES</h3>
      <ul>
        <li><svg width="12" height="12" viewBox="0 0 12 12"><circle cx="6" cy="6" r="6" fill="#fff"/><path d="M3 6.2 L5.2 8.2 L9 4" stroke="#3498db" stroke-width="1.6" fill="none"/></svg>Security Policy</li>
        <li><svg width="12" height="12" viewBox="0 0 12 12"><circle cx="6" cy="6" r="6" fill="#fff"/><path d="M3 6.2 L5.2 8.2 L9 4" stroke="#3498db" stroke-width="1.6" fill="none"/></svg>Privacy Policy</li>
        <li><svg width="12" height="12" viewBox="0 0 12 12"><circle cx="6" cy="6" r="6" fill="#fff"/><path d="M3 6.2 L5.2 8.2 L9 4" stroke="#3498db" stroke-width="1.6" fill="none"/></svg>Terms of Use</li>
        <li><svg width="12" height="12" viewBox="0 0 12 12"><circle cx="6" cy="6" r="6" fill="#fff"/><path d="M3 6.2 L5.2 8.2 L9 4" stroke="#3498db" stroke-width="1.6" fill="none"/></svg>Email Policy</li>
      </ul>
    </div>
    <div class="footer-rule"></div>
    <p class="legal">Harbora NMLS #410286. Click here to view our licensing with the NMLS and DRE<br>2009-2020 Copyright Harbora, Inc. All rights reserved. Lending services provided by Harbora, Inc dba Harbora. Rates, program terms and conditions are subject to change without notice.</p>
    <div class="footer-brand">Harbora</div>
  </footer>

</div>
</body>
</html>
```